BRISKLAND ELECTRICAL SIGN

We are wanting a sign to mount on the side of the road to attract peoples attention, it will be 1200mm high by 2400mm wide. We want it to stand out from the others, modern sharp looking, We are an electrical contractor who wants to be the market leader and supplier of choice to our current clients and futre clients.

Industry/Entity Type

Electrical

Colors

Designer to choose colors to be used in the design.

Requirements
Must have
• Name: Briskland Electrical
• Our logo as per uploaded files
• The words: Design - Installation - Maintenance
• Freecall: 0800 392 548
• Mobile : 021 947 3152 (delete mobile number if gets to cluttered)
• Web: www.briskland.net.nz
Should not have
• a light bulb, or plug

```html
<!DOCTYPE html>
<html lang="en">
<head>
<meta charset="utf-8">
<title>Briskland Electrical – Roadside Sign</title>
<link rel="stylesheet" href="https://fonts.googleapis.com/css2?family=Source+Sans+3:wght@300;400;600;700&display=swap">
<style>
  :root {
    --brand-blue: #3b65a8;
    --brand-blue-dark: #2d528f;
    --swoosh-blue: #4377c2;
    --brand-green: #a6cf3a;
    --text-white: #ffffff;
    --contact-blue: #3f6fb8;
    --contact-grey: #4d4d4f;
    --panel-white: #ffffff;
    --page-bg: #ffffff;
  }
  * { margin: 0; padding: 0; box-sizing: border-box; }
  html, body {
    width: 1200px; height: 655px; overflow: hidden;
    background: var(--page-bg);
    font-family: "Source Sans 3", "Helvetica Neue", Arial, sans-serif;
  }
  .sign {
    position: absolute; left: 57px; top: 57px;
    width: 1086px; height: 541px;
    background: var(--panel-white);
    overflow: hidden;
  }
  .sign-shapes { position: absolute; inset: 0; }
  .headline-block { position: absolute; left: 43px; top: 78px; color: var(--text-white); }
  .tagline {
    font-weight: 300; font-size: 31px; letter-spacing: 0.5px; line-height: 1;
  }
  .title {
    font-weight: 600; font-size: 68px; line-height: 72px; letter-spacing: 1px;
    margin-top: 12px;
    text-shadow: 2px 3px 4px rgba(0,0,0,0.35);
  }
  .services {
    position: absolute; left: 57px; top: 297px;
    font-weight: 700; font-size: 28px; color: var(--text-white);
    text-shadow: 2px 2px 2px rgba(0,0,0,0.45);
    letter-spacing: 0.2px;
  }
  .services .dot { color: var(--swoosh-blue); font-size: 20px; vertical-align: middle; margin: 0 4px; text-shadow: none; }
  .brand-name {
    position: absolute; left: 50px; top: 468px;
    display: flex; align-items: center; gap: 10px;
    font-weight: 700; font-size: 27px; color: var(--brand-blue);
    letter-spacing: 0.5px;
  }
  .brand-mark { width: 16px; height: 16px; border-radius: 50%; background: var(--brand-green); }
  .freecall {
    position: absolute; left: 457px; top: 487px;
    font-size: 27px; font-weight: 600; color: var(--contact-blue); line-height: 1;
  }
  .freecall .number { font-weight: 700; }
  .website {
    position: absolute; left: 796px; top: 487px;
    font-size: 27px; font-weight: 700; color: var(--contact-grey); line-height: 1;
  }
</style>
</head>
<body>
  <div class="sign">
    <svg class="sign-shapes" width="1086" height="541" viewBox="0 0 1086 541">
      <defs>
        <linearGradient id="field-gradient" x1="0" y1="0" x2="1" y2="1">
          <stop offset="0" stop-color="#3e68ab"/>
          <stop offset="1" stop-color="#37609f"/>
        </linearGradient>
        <linearGradient id="photo-gradient" x1="0" y1="0" x2="1" y2="1">
          <stop offset="0" stop-color="#e8f2fb"/>
          <stop offset="0.55" stop-color="#cfdbe6"/>
          <stop offset="0.8" stop-color="#f3a33a"/>
          <stop offset="1" stop-color="#f08a1c"/>
        </linearGradient>
        <linearGradient id="swoosh-gradient" x1="0" y1="0" x2="0" y2="1">
          <stop offset="0" stop-color="#3f72bd"/>
          <stop offset="0.7" stop-color="#4a7fcb"/>
          <stop offset="1" stop-color="#3b6ab3"/>
        </linearGradient>
      </defs>

      <!-- blue field -->
      <rect class="blue-field" x="0" y="0" width="1086" height="456" fill="url(#field-gradient)"
            role="img" aria-label="Faint background of electricity pylons in blue"/>

      <!-- green edge of swoosh -->
      <path class="swoosh-green" fill="var(--brand-green)"
            d="M 640,0 C 565,60 560,220 600,330 C 640,420 700,440 760,456 L 800,456 C 720,430 660,390 640,340 C 605,260 610,90 690,0 Z"/>
      <!-- blue swoosh band -->
      <path class="swoosh-blue" fill="url(#swoosh-gradient)"
            d="M 660,0 C 590,60 585,220 620,320 C 660,410 720,440 780,456 L 880,456 C 790,430 720,380 690,320 C 650,240 645,80 700,0 Z"/>
      <!-- photo area -->
      <path class="photo" fill="url(#photo-gradient)"
            role="img" aria-label="Photo of an electrician in hard hat and hi-vis vest with a laptop, looking up at a transmission tower"
            d="M 715,0 C 660,70 660,240 705,330 C 740,400 800,440 880,456 L 1086,456 L 1086,0 Z"/>
      <!-- accent arrow on swoosh -->
      <path fill="var(--brand-green)" d="M 655,258 L 676,225 L 669,268 Z"/>

      <!-- white lower panel with raised left portion -->
      <path class="lower-panel" fill="var(--panel-white)"
            d="M 0,402 L 368,402 L 418,456 L 1086,456 L 1086,541 L 0,541 Z"/>
      <path class="panel-stripe" fill="var(--brand-green)"
            d="M 368,402 L 390,402 L 436,456 L 418,456 Z"/>

      <!-- services bar -->
      <rect x="42" y="296" width="468" height="42" fill="var(--brand-green)"/>
      <path fill="var(--brand-green)" d="M 505,296 L 512,296 L 526,338 L 519,338 Z"/>
      <path fill="var(--brand-green)" d="M 507,296 L 512,296 L 526,338 L 521,338 Z" opacity="0"/>
    </svg>

    <div class="headline-block">
      <p class="tagline">PROFESSIONAL &amp; TRUSTED</p>
      <h1 class="title">ELECTRICAL<br>CONTRACTOR</h1>
    </div>

    <p class="services">Design<span class="dot">•</span>Installation<span class="dot">•</span>Maintenance</p>

    <div class="brand-name"><span class="brand-mark"></span>BRISKLAND ELECTRICAL</div>

    <p class="freecall">Freecall: <span class="number">0800 392 548</span></p>
    <p class="website">www.briskland.net.nz</p>
  </div>
</body>
</html>
```